Criminal Defense Law Firm needs Stationary design Theme for a Business Card, Envelope, and Letterhea

Our Law Firm is seeking a general design concept for a business card, letterhead, and Envelope.

Our website is WillowcrestTrialDesk.com

A design for these three items is requested to keep branding in place for the firm. Would like to keep the Firm Colors on the website consistent with our branding on business cards, letterheads, and mailing envelopes #10 size to be exact.

We would like business cards printed front and back with Law firm Colors from website.

Letterhead with law firm colors as well. Design is not limited to just the header, but the footer can be utilized as well for email, website, phone, fax, etc.

Simple #10 envelope consisting of the same design principles set out in the previous two designs.

```html
<!DOCTYPE html>
<html lang="en">
<head>
<meta charset="utf-8">
<title>Willowcrest Trial Law Offices – Business Card</title>
<link href="https://fonts.googleapis.com/css2?family=EB+Garamond:wght@400&family=Montserrat:wght@400;700&display=swap" rel="stylesheet">
<style>
  :root {
    --backdrop: #2b2b2b;
    --charcoal: #3b3b3b;
    --paper: #f7f7f5;
    --gold: #b99a57;
    --ink: #3a3a3a;
    --ink-soft: #6b6b6b;
    --silver: #cfcfcf;
    --ghost: #e6e6e4;
  }
  * { margin: 0; padding: 0; box-sizing: border-box; }
  html, body {
    width: 1200px; height: 900px; overflow: hidden;
    background: var(--backdrop);
  }
  .canvas { position: relative; width: 1200px; height: 900px; }

  .card {
    position: absolute;
    width: 600px; height: 343px;
    box-shadow: 0 14px 34px rgba(0,0,0,.45);
    overflow: hidden;
  }
  .card--back { left: 80px; top: 70px; background: var(--charcoal); }
  .card--front { left: 530px; top: 487px; background: var(--paper); }

  .band { position: absolute; left: 0; width: 100%; height: 14px; background: var(--gold); }
  .card--back .band { bottom: 0; }
  .card--front .band { top: 0; }

  .ghost-ring {
    position: absolute; right: -70px; top: 40px;
    width: 230px; height: 230px; border-radius: 50%;
    border: 3px solid var(--ghost);
  }

  .brand {
    position: absolute;
    display: flex; align-items: center; gap: 18px;
  }
  .card--back .brand { left: 70px; top: 80px; }
  .card--front .brand { left: 36px; top: 64px; }
  .brand__mark {
    width: 56px; height: 56px; border-radius: 50%;
    border: 2px solid var(--gold); flex: none;
  }
  .card--front .brand__mark { border-color: var(--ink); }
  .brand__name {
    font-family: "EB Garamond", Georgia, serif;
    font-size: 30px; line-height: 1.02; letter-spacing: 1.5px;
    text-transform: uppercase;
  }
  .card--back .brand__name { color: var(--silver); }
  .card--front .brand__name { color: var(--ink); }

  .web {
    position: absolute; left: 0; right: 0; top: 232px;
    text-align: center;
    font-family: Montserrat, Arial, sans-serif;
    font-size: 15px; letter-spacing: .6px; color: var(--silver);
  }
  .web__accent { color: var(--gold); }

  .person { position: absolute; left: 36px; top: 208px; font-family: Montserrat, Arial, sans-serif; }
  .person__name { font-weight: 700; font-size: 22px; letter-spacing: 1px; color: var(--ink); }
  .person__title { font-size: 15px; color: var(--ink-soft); margin-top: 1px; }

  .contact {
    position: absolute; left: 36px; bottom: 30px;
    font-family: Montserrat, Arial, sans-serif;
    font-size: 14.5px; color: var(--ink);
    white-space: nowrap;
  }
  .contact__label { color: var(--gold); font-weight: 700; }
</style>
</head>
<body>
<main class="canvas">
  <section class="card card--back" aria-label="Business card back">
    <div class="brand">
      <span class="brand__mark"></span>
      <div class="brand__name">Willowcrest Trial<br>Law Offices</div>
    </div>
    <p class="web">www.<span class="web__accent">willowcresttrialdesk</span>.com</p>
    <div class="band"></div>
  </section>

  <section class="card card--front" aria-label="Business card front">
    <div class="band"></div>
    <span class="ghost-ring"></span>
    <div class="brand">
      <span class="brand__mark"></span>
      <div class="brand__name">Willowcrest Trial<br>Law Offices</div>
    </div>
    <div class="person">
      <p class="person__name">DANIEL OSTRANDER</p>
      <p class="person__title">Attorney</p>
    </div>
    <p class="contact">2417 Cedar Row NW, Larkmoor, NM 87190 · <span class="contact__label">Phone</span>: 555.014.2290</p>
  </section>
</main>
</body>
</html>
```